Brisklane Provisions' Ferrotide Bulk Builder 7200

Brisklane Provisions supplies Health supplements and have been trading since 1975, mainly to Bodybuilders and weightlifters. Over the years our customers have aged and our range extended to compliment their needs, i.e; more general supplements. However this label is for our Ferrotide Bulk Builder 7200. If you look online you will see this product is in a 3ltr white pot the label currently, is a dark brown background label with red and white lettering, red denoted the flavour of strawberry.
We would like the design to look good and more up to date for both men and women. A white background, with no horizontal lines top and bottom.

```html
<!DOCTYPE html>
<html lang="en">
<head>
<meta charset="utf-8">
<title>Brisklane Provisions – Ferrotide Bulk Builder 7200</title>
<link href="https://fonts.googleapis.com/css2?family=Anton&family=Montserrat:wght@500;800;900&display=swap" rel="stylesheet">
<style>
  :root {
    --ink: #1b1b1d;
    --red: #c8162e;
    --red-deep: #7a0d1d;
    --red-dark: #5a0a16;
    --label-light: #f4f4f5;
    --label-mid: #e4e4e6;
    --white: #ffffff;
  }
  * { margin: 0; padding: 0; box-sizing: border-box; }
  html, body { width: 1200px; height: 1200px; overflow: hidden; background: var(--white); }
  .label {
    position: relative;
    width: 1200px; height: 1200px;
    background: radial-gradient(ellipse at 50% 45%, var(--label-light) 0%, var(--label-mid) 100%);
    font-family: 'Montserrat', sans-serif;
    color: var(--ink);
  }
  .brand {
    position: absolute; top: 150px; left: 0; width: 100%;
    text-align: center;
    font-family: 'Montserrat', sans-serif; font-weight: 500;
    font-size: 58px; letter-spacing: 1px; line-height: 1;
    color: var(--ink);
  }
  .brand-sub {
    position: absolute; top: 218px; left: 0; width: 100%;
    text-align: center;
    font-weight: 500; font-size: 40px; letter-spacing: 1px; color: var(--ink);
  }
  .banner {
    position: absolute; top: 320px; left: 170px; width: 560px; height: 70px;
    background: linear-gradient(90deg, var(--red-deep), var(--red) 50%, var(--red-dark));
    clip-path: polygon(6% 0, 100% 0, 92% 100%, 0 100%);
  }
  .banner-text {
    position: absolute; top: 318px; left: 260px;
    font-family: 'Anton', sans-serif; font-size: 66px; line-height: 74px;
    color: var(--white); letter-spacing: 2px;
    transform: skewX(-10deg);
  }
  .title {
    font-family: 'Anton', sans-serif;
    background: linear-gradient(120deg, var(--red-dark) 0%, var(--red) 35%, var(--red-deep) 60%, var(--red) 80%, var(--red-dark) 100%);
    -webkit-background-clip: text; background-clip: text;
    color: transparent;
    -webkit-text-stroke: 4px var(--ink);
    transform: skewX(-8deg);
    line-height: 1;
  }
  .title-main { position: absolute; top: 405px; left: 150px; font-size: 176px; letter-spacing: 2px; }
  .title-number { position: absolute; top: 600px; left: 560px; font-size: 300px; letter-spacing: 4px; }
  .rule {
    position: absolute; top: 800px; left: 150px; width: 440px; height: 30px;
    background: linear-gradient(90deg, var(--red-deep), var(--red) 50%, var(--red-dark));
    clip-path: polygon(4% 0, 100% 0, 96% 100%, 0 100%);
  }
  .servings { position: absolute; top: 840px; left: 170px; text-align: center; }
  .servings-count { font-weight: 900; font-size: 118px; line-height: 1; }
  .servings-label { font-weight: 800; font-size: 40px; line-height: 1.1; }
  .flavour {
    position: absolute; top: 900px; left: 640px;
    font-weight: 900; font-size: 56px; letter-spacing: 1px; color: var(--red);
  }
  .footer-bar {
    position: absolute; top: 1020px; height: 56px;
    background: linear-gradient(90deg, var(--red-dark), var(--red) 55%, var(--red-deep));
    clip-path: polygon(8% 0, 100% 0, 92% 100%, 0 100%);
    color: var(--white); font-weight: 800; font-size: 28px;
    display: flex; align-items: center; justify-content: center;
  }
  .footer-left { left: 140px; width: 440px; }
  .footer-mid { left: 620px; width: 110px; }
  .footer-right { left: 760px; width: 430px; }
</style>
</head>
<body>
  <main class="label">
    <div class="brand">BRISKLANE</div>
    <div class="brand-sub">PROVISIONS</div>

    <div class="banner"></div>
    <div class="banner-text">FERROTIDE</div>

    <div class="title title-main">BULK BUILDER</div>
    <div class="title title-number">7200</div>

    <div class="rule"></div>
    <div class="servings">
      <div class="servings-count">30</div>
      <div class="servings-label">SERVING</div>
    </div>

    <div class="flavour">STRAWBERRY</div>

    <div class="footer-bar footer-left">DIETARY SUPPLEMENT</div>
    <div class="footer-bar footer-mid"></div>
    <div class="footer-bar footer-right">NET WT. 260 G ( 9.2 oz )</div>
  </main>
</body>
</html>
```